Coffee Shop needs a fresh new menu

Hi,
I would like a new menu to be designed for our coffee shop.
We display our menu on a television screen, so would need it in a file that would allow us to continue to do so -- I have attached a photo so that you can see our current design, and how it is displayed.

I'd like something that is easy to read, if the design could have a "hipster" feel to it -- we are located at a hospital and University.

I have attached a Word file with what we would like on the menu.

Feel free to contact me if you have any questions.

Thanks,
Liv

Just A4 size will be fine, and no need to include menu 1 and menu 2 - I just put them in as an example of what we already have -- they are our printed menu's. Thanks

Hospital

```html
<!DOCTYPE html>
<html lang="en">
<head>
<meta charset="utf-8">
<title>Restaurant Menu</title>
<link rel="stylesheet" href="https://fonts.googleapis.com/css2?family=Tinos:ital,wght@1,400&display=swap">
<style>
  :root {
    --green-light: #a6d95a;
    --green-mid: #6cc23a;
    --green-deep: #2f9e3a;
    --panel-fill: #fefbd2;
    --panel-border: #1a1a1a;
    --heading-red: #c1272d;
    --ink: #1c1c1c;
    --white: #ffffff;
    --cup-brown: #8a5a2e;
    --bread-tan: #d9a25a;
    --plate-white: #f2f2f2;
    --cake-pink: #e7a7bd;
  }
  * { margin: 0; padding: 0; box-sizing: border-box; }
  html, body { width: 1200px; height: 848px; overflow: hidden; }
  body {
    position: relative;
    font-family: "Tinos", "Times New Roman", serif;
    font-style: italic;
    color: var(--ink);
    background: radial-gradient(ellipse at 62% 48%, var(--green-light) 0%, var(--green-mid) 45%, var(--green-deep) 100%);
  }
  .menu-title {
    position: absolute;
    left: 62px;
    top: 840px;
    transform: rotate(-90deg);
    transform-origin: 0 0;
    font-size: 104px;
    font-weight: 400;
    line-height: 1;
    color: var(--white);
    white-space: nowrap;
  }
  .panel {
    position: absolute;
    background: var(--panel-fill);
    border: 2px solid var(--panel-border);
    border-radius: 28px;
  }
  .panel--coffee { left: 228px; top: 24px; width: 438px; height: 424px; }
  .panel--hot { left: 690px; top: 24px; width: 438px; height: 424px; }
  .panel--light { left: 226px; top: 467px; width: 438px; height: 304px; }
  .panel--breakfast { left: 690px; top: 467px; width: 438px; height: 304px; }

  .panel-heading {
    position: absolute;
    font-size: 23px;
    font-weight: 400;
    color: var(--heading-red);
    white-space: nowrap;
  }
  .item-list {
    position: absolute;
    list-style: none;
    font-size: 17.5px;
    line-height: 22.9px;
    white-space: nowrap;
  }
  .item-list .gap { height: 22.9px; }
  .price-row { display: grid; grid-template-columns: 140px 112px auto; }

  .panel--coffee .panel-heading { left: 21px; top: 24px; }
  .panel--coffee .item-list { left: 21px; top: 72px; }
  .panel--hot .panel-heading { left: 21px; top: 30px; }
  .panel--hot .item-list { left: 21px; top: 77px; }
  .panel--light .panel-heading { left: 52px; top: 18px; }
  .panel--light .item-list { left: 52px; top: 67px; }
  .panel--breakfast .panel-heading { left: 35px; top: 25px; }
  .panel--breakfast .item-list { left: 35px; top: 73px; }

  .illustration { position: absolute; border-radius: 18px; }
  .illustration--coffee-cup { left: 583px; top: 272px; width: 68px; height: 176px; background: linear-gradient(180deg, #cdb9a0 0%, var(--cup-brown) 100%); border-radius: 10px; }
  .illustration--sandwich { left: 975px; top: 305px; width: 165px; height: 142px; background: linear-gradient(160deg, #f3ddb0 0%, var(--bread-tan) 60%, #b8553a 100%); }
  .illustration--breakfast-plate { left: 466px; top: 683px; width: 202px; height: 122px; background: radial-gradient(ellipse at 50% 55%, #f7e9a8 0%, var(--plate-white) 55%, #c9c9c9 100%); border-radius: 50%; }
  .illustration--cupcakes { left: 953px; top: 702px; width: 210px; height: 98px; background: linear-gradient(180deg, var(--cake-pink) 0%, #c98a9c 60%, #5a3a2a 100%); border-radius: 30px; }

  .extras {
    position: absolute;
    left: 250px;
    top: 788px;
    color: var(--white);
    white-space: nowrap;
  }
  .extras-title { font-size: 21px; line-height: 26px; }
  .extras-note { font-size: 16.5px; line-height: 24px; }
</style>
</head>
<body>
  <h1 class="menu-title">Restaurant Menu</h1>

  <section class="panel panel--coffee">
    <h2 class="panel-heading">Coffee:</h2>
    <ul class="item-list">
      <li class="price-row"><span>Latte</span><span>small $4.0</span><span>large $4.50</span></li>
      <li class="price-row"><span>Cappuccino</span><span>small $4.0</span><span>large $4.50</span></li>
      <li class="price-row"><span>Flat white</span><span>small $4.0</span><span>large $4.50</span></li>
      <li class="price-row"><span>Long black</span><span>small $4.0</span><span>large $4.50</span></li>
      <li class="price-row"><span>Hot chocolate</span><span>small $4.0</span><span>large $4.50</span></li>
      <li class="gap"></li>
      <li class="price-row"><span>Chai latte</span><span>small $4.50</span><span>large $5.0</span></li>
      <li class="price-row"><span>mocha</span><span>small $4.50</span><span>large $5.0</span></li>
      <li class="price-row"><span>dirty chai</span><span>small $5</span><span>large $5.50</span></li>
      <li class="gap"></li>
      <li>Espresso $3.50</li>
      <li>Short macchiato $4.0</li>
      <li>piccolo $4.0</li>
      <li>long macchiato $4.50</li>
    </ul>
  </section>
  <div class="illustration illustration--coffee-cup" role="img" aria-label="Illustration of a steaming takeaway coffee cup"></div>

  <section class="panel panel--hot">
    <h2 class="panel-heading">Hot food and sandwiches:</h2>
    <ul class="item-list">
      <li>Pre made sandwiches $6.50 - $7.50</li>
      <li>Pre made focaccias $8.50</li>
      <li>Wraps $7.50</li>
      <li>Vegetarian salad $7.50</li>
      <li>Meat/seafood salad $9.50</li>
      <li>Hot chips $4.50</li>
      <li>Dim sim $1.50</li>
      <li>Potato cake $1.50</li>
      <li>Plain hamburger $7.50</li>
      <li>Hamburger with the lot $9.0</li>
      <li>chicken schnitzel burger $8.50</li>
    </ul>
  </section>
  <div class="illustration illustration--sandwich" role="img" aria-label="Illustration of a layered sandwich"></div>

  <section class="panel panel--light">
    <h2 class="panel-heading">Something light:</h2>
    <ul class="item-list">
      <li>Mixed yoghurts $5.50</li>
      <li>Chia pudding $5.50</li>
      <li>Fruit salad $5.50</li>
      <li>Bircher muesli $5.50</li>
      <li>Protein balls&nbsp; $4.0</li>
      <li>banana bread $4.50</li>
      <li>Muffins $4.50</li>
      <li>Slices $4.0</li>
    </ul>
  </section>
  <div class="illustration illustration--breakfast-plate" role="img" aria-label="Illustration of a breakfast plate with eggs, toast and bacon"></div>

  <section class="panel panel--breakfast">
    <h2 class="panel-heading">Breakfast items:</h2>
    <ul class="item-list">
      <li>Bacon, Egg and Cheese Roll $6.0</li>
      <li>Ham and Cheese Toastie $5.0</li>
      <li>Cheese and Tomato Toastie $5.0</li>
      <li>Ham and Cheese Croissant $6.0</li>
      <li>Cheese and Tomato Croissant $5.50</li>
      <li>Plain Croissant $3.50</li>
      <li>Hash Brown $2.0</li>
      <li>2 Piece Toast $3.0</li>
      <li>2 Piece Rasin Toast $3.0</li>
    </ul>
  </section>
  <div class="illustration illustration--cupcakes" role="img" aria-label="Illustration of a tray of pink frosted cupcakes"></div>

  <footer class="extras">
    <p class="extras-title">Extras</p>
    <p class="extras-note">Soy Milk/Lactose Free Milk/Syrups/Extra Shot/Decaf&nbsp; $0.50 extra</p>
  </footer>
</body>
</html>
```